We had a great little logo for the start up of our small business. We have just received word from lawyers that a term we used was trademarked. We now have a new title and need to edit our logo asap plus...
Letterhead - For Outlook and Word
Business Card
Email Signature - for Outlook
Our tagline will now be "We Take The Mess. You Keep The Fresh"
Email - tovi@corlewlnl.example
Phone - +61482 915 627
Website - http://corlewlnl.example
Location - 12 Fenmore Drive, Dunsworth 6391, Western Australia
Title - General Manager
Name - Tovi Reskander
Target Market(s)
Australian hospitality businesses requiring prompt, professional and personalized service. This service is dedicated to hiring and laundering of linen for commercial businesses such as hotels, restaurants, bed and breakfasts. We intend for it to branch out to personal items and cleaning in the future.
Look and feel
Each slider illustrates characteristics of the customer's brand and the style your logo design should communicate.

```html
<!DOCTYPE html>
<html lang="en">
<head>
<meta charset="utf-8">
<title>Corlew Linen &amp; Laundry — Business Card</title>
<link rel="stylesheet" href="https://fonts.googleapis.com/css2?family=Open+Sans:wght@400;600;700&display=swap">
<style>
  :root {
    --brand-green: #4ca63a;
    --brand-blue: #1c66b0;
    --ink: #4a4a4a;
    --ink-soft: #8a8a8a;
    --card: #ffffff;
    --backdrop: #ece9e4;
    --rule: #d6d6d6;
  }
  * { box-sizing: border-box; margin: 0; padding: 0; }
  html, body { width: 1200px; height: 720px; overflow: hidden; }
  body {
    background: var(--backdrop);
    font-family: "Open Sans", sans-serif;
    color: var(--ink);
  }
  .canvas {
    position: relative;
    width: 1200px;
    height: 720px;
    display: flex;
    align-items: center;
    justify-content: center;
    gap: 40px;
  }
  .card {
    position: relative;
    width: 520px;
    height: 318px;
    background: var(--card);
    box-shadow: 0 2px 10px rgba(0,0,0,0.12);
    overflow: hidden;
  }

  .brand { display: flex; align-items: center; gap: 10px; }
  .brand-dot {
    width: 16px; height: 16px; border-radius: 50%;
    background: var(--brand-green); flex: none;
  }
  .brand-name {
    font-weight: 700;
    color: var(--brand-green);
    white-space: nowrap;
    letter-spacing: -0.2px;
  }
  .brand-strap {
    font-size: 10px;
    letter-spacing: 2.4px;
    color: var(--ink-soft);
    margin-top: 4px;
  }

  .card--contact .brand-block {
    position: absolute; top: 36px; right: 44px; text-align: right;
  }
  .card--contact .brand-name { font-size: 26px; }
  .card--contact .brand { justify-content: flex-end; }

  .contact {
    position: absolute; top: 138px; left: 0; right: 0;
    display: flex; justify-content: center;
  }
  .contact-person {
    text-align: right; padding-right: 18px;
    border-right: 1px solid var(--rule);
    font-size: 12.5px; line-height: 1.45;
  }
  .contact-name {
    font-size: 16px; font-weight: 700; color: var(--brand-green);
  }
  .contact-lines {
    list-style: none; padding-left: 14px;
    font-size: 12.5px; line-height: 1.85;
  }
  .contact-lines li { display: flex; align-items: center; gap: 7px; }
  .contact-icon { width: 14px; height: 14px; flex: none; }

  .card-band { position: absolute; left: 0; bottom: 0; width: 520px; height: 70px; }

  .card--message {
    display: flex; flex-direction: column; align-items: center; justify-content: center;
  }
  .card--message .brand-name { font-size: 34px; }
  .card--message .brand-block { text-align: center; }
  .tagline {
    margin-top: 30px;
    font-size: 21px; font-weight: 600; color: var(--brand-blue);
  }
  .site {
    margin-top: 16px;
    font-size: 15px; letter-spacing: 3px; color: var(--ink);
  }
  .site strong { color: var(--brand-green); font-weight: 700; }
</style>
</head>
<body>
<main class="canvas">

  <section class="card card--contact" aria-label="Business card, contact side">
    <div class="brand-block">
      <div class="brand">
        <span class="brand-dot"></span>
        <span class="brand-name">Corlew Linen &amp; Laundry</span>
      </div>
      <p class="brand-strap">Keeping the coast crisp</p>
    </div>

    <div class="contact">
      <div class="contact-person">
        <p class="contact-name">Tovi Reskander</p>
        <p>General Manager</p>
        <p>12 Fenmore Drive</p>
        <p>Dunsworth 6391, Western Australia</p>
      </div>
      <ul class="contact-lines">
        <li>
          <svg class="contact-icon" viewBox="0 0 14 14" aria-hidden="true">
            <circle cx="7" cy="7" r="7" fill="var(--brand-green)"/>
            <path d="M4.4 3.6l1.4-.3.8 1.8-.9.7a5 5 0 0 0 2.5 2.5l.7-.9 1.8.8-.3 1.4c-3.4.3-6.3-2.6-6-6z" fill="#fff"/>
          </svg>+61482 915 627</li>
        <li>
          <svg class="contact-icon" viewBox="0 0 14 14" aria-hidden="true">
            <circle cx="7" cy="7" r="7" fill="var(--brand-green)"/>
            <rect x="3.5" y="4.5" width="7" height="5" fill="#fff"/>
            <path d="M3.5 4.7L7 7.4l3.5-2.7" fill="none" stroke="var(--brand-green)" stroke-width=".8"/>
          </svg>tovi@corlewlnl.example</li>
        <li>
          <svg class="contact-icon" viewBox="0 0 14 14" aria-hidden="true">
            <circle cx="7" cy="7" r="7" fill="var(--brand-green)"/>
            <circle cx="7" cy="7" r="3.6" fill="none" stroke="#fff" stroke-width=".9"/>
            <path d="M3.4 7h7.2M7 3.4c-1.6 2-1.6 5.2 0 7.2M7 3.4c1.6 2 1.6 5.2 0 7.2" fill="none" stroke="#fff" stroke-width=".7"/>
          </svg>www.corlewlnl.example</li>
      </ul>
    </div>

    <svg class="card-band" viewBox="0 0 520 70" preserveAspectRatio="none" aria-hidden="true">
      <polygon points="0,56 330,56 340,70 0,70" fill="var(--brand-green)"/>
      <polygon points="330,56 520,8 520,70 340,70" fill="var(--brand-blue)"/>
      <polygon points="300,56 520,4 520,8 330,56" fill="var(--brand-green)"/>
    </svg>
  </section>

  <section class="card card--message" aria-label="Business card, message side">
    <div class="brand-block">
      <div class="brand">
        <span class="brand-dot"></span>
        <span class="brand-name">Corlew Linen &amp; Laundry</span>
      </div>
      <p class="brand-strap">Keeping the coast crisp</p>
    </div>
    <p class="tagline">We Take The Mess. You Keep The Fresh</p>
    <p class="site">www.<strong>corlewlnl</strong>.example</p>
  </section>

</main>
</body>
</html>
```